This book will apply the 12 Steps to gaming addiction, also known as video game addiction. The primary purpose of the book is to provide an effective solution for this new type of addiction. The solution is based on the rich and successful concepts of traditional twelve-step programs like RL.

The title on the cover will be "Nine Doors Past the Glowing Screen" and "by Martin Quorby". A subtitle can be used if it works in your design of "A Practical Path Beyond Compulsive Console Play". Cover will be for a 6" x 9" book approximately 110 pages in length.

Some back cover text including some review quotes and an author bio are in the attached Word doc. There is also an author photo attached for for the back cover.

Requirements
Must have
• For the cover design it could be stylized, or an image, a partial image, or whatever. I am open to suggestions. Think about what would be noticed by a person searching for help with moderating their video game use, or by the parents or loved ones of problem gamers. Something contemporary and eye catching.

```html
<!DOCTYPE html>
<html lang="en">
<head>
<meta charset="utf-8">
<title>Nine Doors Past the Glowing Screen – Book Cover</title>
<link href="https://fonts.googleapis.com/css2?family=Russo+One&family=Tinos:wght@400;700&display=swap" rel="stylesheet">
<style>
  :root{
    --stage:#e9e7e3;
    --cover:#1b1b1d;
    --spine-edge:#2c2c30;
    --cyan:#26d4ec;
    --cyan-soft:#7fdcea;
    --red:#ec2430;
    --art-deep:#0c1a2a;
    --art-blue:#1f4f86;
    --art-red:#5a1a24;
  }
  *{margin:0;padding:0;box-sizing:border-box}
  html,body{width:1200px;height:675px;overflow:hidden;background:var(--stage)}
  .stage{position:relative;width:1200px;height:675px}

  .cover{position:absolute;top:94px;width:345px;height:478px;background:var(--cover);
    border-right:4px solid var(--spine-edge)}
  .back{left:207px}
  .front{left:647px;border-right:none;border-left:4px solid var(--spine-edge)}

  /* back cover */
  .back-copy{position:absolute;left:31px;top:23px;width:290px;
    font-family:"Tinos",serif;font-size:6.5px;line-height:1.27;color:var(--cyan-soft)}
  .back-copy h2{font-size:6.8px;font-weight:700;color:var(--cyan);margin-bottom:8px}
  .back-copy p{margin-bottom:8px}
  .back-copy .attrib{display:block}
  .back-copy .about{margin-top:16px}
  .author-photo{position:absolute;left:125px;top:372px;width:102px;height:90px}

  /* front cover */
  .title{position:absolute;left:0;right:0;top:20px;text-align:center;
    font-family:"Russo One",sans-serif;color:var(--cyan);line-height:1;
    transform:skewX(-10deg)}
  .title .line-big{display:block;font-size:36px;letter-spacing:.5px}
  .title .accent{color:var(--red)}
  .title .line-mid{display:block;font-size:16px;margin:6px 0 4px}
  .title .line-xl{display:block;font-size:33px}
  .subtitle{position:absolute;left:0;right:0;top:163px;text-align:center;
    font-family:"Russo One",sans-serif;font-size:6.4px;color:var(--red);
    letter-spacing:.2px;transform:skewX(-10deg)}
  .cover-art{position:absolute;left:0;top:176px;width:341px;height:260px}
  .author{position:absolute;left:0;right:0;bottom:22px;text-align:center;
    font-family:"Russo One",sans-serif;font-size:17px;color:var(--red);
    transform:skewX(-10deg)}
</style>
</head>
<body>
<main class="stage">

  <section class="cover back">
    <div class="back-copy">
      <h2>Praise for Nine Doors Past the Glowing Screen</h2>
      <p>“A must-read for anyone who is addicted to or thinks they may have a problem with digital gaming. This eloquent work will also be useful to academics and clinicians exploring potential solutions. The author recognizes the similarities between gaming addiction and other addictions, and logically applies one of the most effective known solutions for addiction - The Twelve Steps.”
        <span class="attrib">-- Dale Wrenfield, Noted Interventionist and Keynote Speaker</span></p>
      <p>“If you suffer from digital gaming addiction, I strongly encourage you to use this book as your road map to get you back to the real world.”
        <span class="attrib">-- Owen Prattley, Founder of Signal Feed Review</span></p>
      <p>“As a high school teacher for 24 years, husband, father, coach, and 12-Step member, I can assure you that this book will transform the life of anyone who is addicted to video games. Well written, easy to understand, and a wonderful book that will provide you with a clear road map to recovery, and this includes teenagers, a group I have been working with in the classroom for decades.”
        <span class="attrib">-- Lionel Barrows, Harbor Vale, CA High School Teacher</span></p>
      <p>******** OR SOME OTHER BREAK TO SEPARATE SECTIONS</p>
      <p>An effective solution to the challenge of Digital Gaming Addiction (aka Video Game Addiction) based on the rich and successful tradition of the Twelve Steps.</p>
      <p>Addiction to Digital Gaming is a new and troubling phenomenon that has burst upon an unprepared society with alarming speed. Many people crave the use of Digital Games in a strikingly similar way to any other addict. Digital Games are a complex software and hardware system that have been designed to promote continued and progressive usage. This sophisticated technology clearly feeds on natural addictive tendencies.</p>
      <p>The 12 Steps are one of the most effective methods for treating addiction in human history. Originating with Recovery League in 1939, the 12 Steps have since been used to treat a variety of other addictions, including drugs, sex, gambling, eating disorders, and many others. Now in this groundbreaking work the 12 Steps are applied to the complex and evolving contemporary phenomenon of Digital Gaming Addiction.</p>
      <h2 class="about">About the Author</h2>
      <p>Marty Quorby is a Technology Consultant and Writer with many years of professional coding and consulting experience. He also struggled with addiction to drugs and alcohol and is now clean and sober in a Twelve-Step program for over 17 years. This unique combination of 12-Step experience and technology expertise led him to create Nine Doors Past the Glowing Screen.</p>
    </div>
    <svg class="author-photo" viewBox="0 0 102 90" role="img" aria-label="Author portrait photograph in a hexagon frame">
      <defs>
        <linearGradient id="photoTone" x1="0" y1="0" x2="0" y2="1">
          <stop offset="0" stop-color="#6f8a5e"/>
          <stop offset="1" stop-color="#2a3140"/>
        </linearGradient>
      </defs>
      <polygon points="26,1 76,1 101,45 76,89 26,89 1,45" fill="url(#photoTone)" stroke="var(--cyan)" stroke-width="1.5"/>
    </svg>
  </section>

  <section class="cover front">
    <h1 class="title">
      <span class="line-big">NINE <span class="accent">DOORS</span></span>
      <span class="line-mid">PAST THE GLOWING</span>
      <span class="line-xl">SCREEN</span>
    </h1>
    <p class="subtitle">A PRACTICAL PATH BEYOND COMPULSIVE CONSOLE PLAY</p>
    <svg class="cover-art" viewBox="0 0 341 260" role="img" aria-label="Illustration of a hooded gamer holding a controller under glowing red 'game over' screen text">
      <defs>
        <radialGradient id="artGlow" cx="0.5" cy="0.45" r="0.6">
          <stop offset="0" stop-color="var(--art-blue)"/>
          <stop offset="0.45" stop-color="var(--art-red)" stop-opacity="0.55"/>
          <stop offset="1" stop-color="var(--cover)"/>
        </radialGradient>
      </defs>
      <rect width="341" height="260" fill="url(#artGlow)"/>
    </svg>
    <p class="author">MARTIN QUORBY</p>
  </section>

</main>
</body>
</html>
```